Business card design needed

My company does everything from wiring up your exisiting entertainment system, to installing a complete new system for you. We can mount your plasma on the wall, install an aerial point for you, setup some surround sound in your outdoor area or install a new cinema room in your house. Any Audio or Visual requirements you may have we can provide these for you. If you want to have a party to remember at your place or just some chilled sounds by the pool, we can give you just the right size system.

Industry/Entity Type

Entertainment

Contact Information for Business Card

The Sound Crew
Declan Whitford
e| declan@thesoundcrewqz.com.au
w| www.thesoundcrewqz.com.au
m| 0412 576 018

Requirements
Must have
• The logo that i have uploaded is just a starter...something similar to this but not exact or any new suggestions you have would be great too. Colour choice we are pretty easy on we did think Red and Yellow but happy to take advice, something that stands out from the rest i guess.

```html
<!DOCTYPE html>
<html lang="en">
<head>
<meta charset="utf-8">
<title>The Sound Crew — Business Card</title>
<link rel="stylesheet" href="https://fonts.googleapis.com/css2?family=PT+Sans+Narrow:wght@400;700&display=swap">
<style>
  :root {
    --page: #ffffff;
    --brand-red: #e60a28;
    --ink: #000000;
    --mark-dark: #2e0000;
  }
  html, body {
    margin: 0;
    padding: 0;
    width: 1000px;
    height: 1200px;
    overflow: hidden;
    background: var(--page);
    font-family: "PT Sans Narrow", "Arial Narrow", sans-serif;
  }
  .card {
    position: absolute;
    left: 254px;
    top: 207px;
    width: 507px;
    height: 878px;
  }
  .card-top {
    position: absolute;
    left: 0; top: 0;
    width: 100%;
    height: 564px;
    background: var(--brand-red);
  }
  .brand-mark {
    position: absolute;
    left: 0; right: 0;
    top: 250px;
    display: flex;
    justify-content: center;
    align-items: center;
    gap: 14px;
  }
  .brand-mark-dot {
    width: 26px;
    height: 26px;
    border-radius: 50%;
    background: var(--mark-dark);
  }
  .brand-mark-name {
    font-weight: 700;
    font-size: 54px;
    line-height: 1;
    color: var(--mark-dark);
  }
  .company-name {
    position: absolute;
    left: 0; right: 0;
    top: 482px;
    margin: 0;
    text-align: center;
    font-weight: 700;
    font-size: 42px;
    line-height: 1;
    color: var(--ink);
  }
  .card-bottom {
    position: absolute;
    left: 0; top: 564px;
    width: 100%;
    height: 314px;
    background: var(--ink);
  }
  .person-name {
    position: absolute;
    left: 0; right: 0;
    top: 44px;
    margin: 0;
    text-align: center;
    font-weight: 700;
    font-size: 35px;
    line-height: 1;
    color: var(--brand-red);
  }
  .contact-list {
    position: absolute;
    left: 80px;
    top: 118px;
    margin: 0;
    padding: 0;
    list-style: none;
    color: var(--brand-red);
    font-size: 31px;
    line-height: 1;
  }
  .contact-item {
    display: flex;
    align-items: center;
    height: 55px;
  }
  .contact-label {
    width: 26px;
    text-align: right;
  }
  .contact-divider {
    width: 2px;
    height: 36px;
    margin: 0 8px 0 6px;
    background: var(--brand-red);
  }
</style>
</head>
<body>
  <div class="card">
    <section class="card-top">
      <div class="brand-mark">
        <span class="brand-mark-dot"></span>
        <span class="brand-mark-name">The Sound Crew</span>
      </div>
      <h1 class="company-name">The Sound Crew</h1>
    </section>
    <section class="card-bottom">
      <h2 class="person-name">Declan Whitford</h2>
      <ul class="contact-list">
        <li class="contact-item"><span class="contact-label">e</span><span class="contact-divider"></span><span>declan@thesoundcrewqz.com.au</span></li>
        <li class="contact-item"><span class="contact-label">w</span><span class="contact-divider"></span><span>www.thesoundcrewqz.com.au</span></li>
        <li class="contact-item"><span class="contact-label">m</span><span class="contact-divider"></span><span>0412 576 018</span></li>
      </ul>
    </section>
  </div>
</body>
</html>
```